Harbor Mortgage Relief

Please help us give our website a remake or a FACELIFT. It is not very good but it says what we need it to say. But the design is terrible.
I would like our new design font and logo to be used as the theme.

I also want more photos on the site.

I also want consistency with the pages so they look clean.

We want the professionals to do this, let's see what you got!

Thank you!
Updates

Project Deadline Extended
Reason: I can understand you want to be paid. So I will commit to the fee but I want you to have time to make a KICK ASS website for me dudes! Thanks

HI!  Just wanted to say thanks for your time on these.  A lot are great.  However the firefighters have nothing to do with Foreclosure.  We are saving peoples homes from the bank taking them and selling them.   I LOVE the house photos and the families on the website.  That is the direction we like.  THanks.

THANK U ALL FOR THE WORK!   I like a few ending in the numbers: 147  733  693  536  620  478  727  508     I will go over them and choose one soon.  Thank you.   You will be paid shortly. 

Requirements
Must have
• Bright, Upbeat photos. Color scheme should be in order. We like icons on the bottom. not just text.

```html
<!DOCTYPE html>
<html lang="en">
<head>
<meta charset="utf-8">
<title>Harbor Mortgage Relief</title>
<link href="https://fonts.googleapis.com/css2?family=Open+Sans:ital,wght@0,400;0,600;0,700;0,800;1,400;1,600&display=swap" rel="stylesheet">
<style>
:root{
  --red:#e0252b;
  --red-dark:#c81c22;
  --ink:#2b2b2b;
  --text:#5a5a5a;
  --muted:#8a8a8a;
  --page:#eef0f4;
  --panel:#ffffff;
  --line:#dcdde0;
  --green:#5fae1e;
  --green-dark:#4a8f14;
  --footer-top:#3a3a3a;
  --footer-bottom:#1c1c1c;
}
*{box-sizing:border-box;margin:0;padding:0}
html,body{width:1028px;height:1200px;overflow:hidden}
body{background:var(--page);font-family:"Open Sans",Arial,sans-serif;color:var(--text);position:relative}
a{color:inherit;text-decoration:none}

.site-header{position:absolute;left:0;top:0;width:1028px;height:100px}
.brand{position:absolute;left:132px;top:26px;display:flex;align-items:center;gap:10px}
.brand-dot{width:50px;height:50px;border-radius:50%;background:var(--red)}
.brand-name{font-weight:800;font-size:17px;line-height:19px;color:var(--red);text-transform:uppercase;letter-spacing:.2px}
.hotline{position:absolute;right:128px;top:22px;font-size:17px;color:#555;display:flex;align-items:center;gap:8px}
.hotline strong{color:var(--red);font-weight:700;font-size:21px;display:flex;align-items:center;gap:4px}
.main-nav{position:absolute;left:458px;top:61px;display:flex;gap:4px}
.main-nav a{display:block;height:28px;line-height:28px;padding:0 14px;font-size:11px;color:#555;background:linear-gradient(#fff,#ececec);border:1px solid var(--line);text-transform:uppercase}
.main-nav a.is-active{background:linear-gradient(#4a4a4a,#262626);color:#fff;border-color:#222}

.hero{position:absolute;left:126px;top:103px;width:774px;height:324px;background:linear-gradient(135deg,#7fa35a 0%,#d9c9a5 35%,#f2e6b8 60%,#9cb07a 100%)}
.consult{position:absolute;left:513px;top:180px;width:261px;height:103px;background:var(--red);padding:11px 14px 0;color:#fff}
.consult h2{font-size:17px;font-weight:400;line-height:20px;white-space:nowrap}
.consult h2 b{font-weight:800}
.consult p{font-size:8px;line-height:11px;opacity:.95;white-space:nowrap}
.consult-form{display:flex;margin-top:10px;width:233px}
.consult-form span{flex:0 0 126px;height:30px;background:#fff;color:#333;font-size:11px;font-weight:600;line-height:30px;padding-left:12px}
.consult-form b{flex:1;height:30px;background:linear-gradient(#3a3a3a,#1e1e1e);font-size:12px;line-height:30px;text-align:center}

.feature-band{position:absolute;left:0;top:427px;width:1028px;height:61px;background:rgba(255,255,255,.6)}
.features{position:absolute;left:126px;top:427px;width:774px;height:61px;display:flex;background:#f7f7f7;border:1px solid #e4e4e4}
.feature{flex:1;display:flex;align-items:center;gap:12px;padding-left:20px;font-size:11px;line-height:14px;color:#444;border-right:1px solid #e1e1e1}
.feature:last-child{border-right:0}
.feature.is-active{background:#fff}
.feature svg{flex:0 0 32px}

.sidebar{position:absolute;left:126px;top:510px;width:218px;height:452px;background:var(--panel);border:1px solid #e2e2e2;box-shadow:0 1px 4px rgba(0,0,0,.08);padding:12px 15px}
.side-title{font-size:13px;font-weight:700;color:#333;text-transform:uppercase;white-space:nowrap}
.side-title span{color:var(--red)}
.side-title.normal{text-transform:none}
.side-title.normal span{text-transform:uppercase}
.quote{font-size:9.5px;line-height:13px;color:#666;margin-top:10px;text-align:justify}
.quote::before{content:"\201C";font-size:20px;font-weight:700;color:#999;vertical-align:-6px;margin-right:3px}
.quote a{color:var(--red)}
.author{display:flex;gap:10px;align-items:center;margin-top:10px}
.author-photo{width:30px;height:30px;background:linear-gradient(#c99b7a,#8b5e44)}
.author b{display:block;color:var(--red);font-weight:400;font-size:11px;line-height:14px}
.author small{font-size:9px;color:#777}
.btn{display:inline-block;background:linear-gradient(var(--green),var(--green-dark));color:#fff;font-size:9px;font-weight:700;text-transform:uppercase;padding:5px 10px}
.btn::after{content:" \25B8"}
.sidebar .btn{margin-top:10px}
.mission-title{margin-top:18px}
.mission-photo{margin-top:10px;height:96px;background:linear-gradient(90deg,#caa48a,#e9e6e2 45%,#6d6f76);border:3px solid #fff;box-shadow:0 2px 5px rgba(0,0,0,.25)}
.mission-text{font-size:9.5px;line-height:13px;color:#555;margin-top:10px}

.content{position:absolute;left:367px;top:510px;width:533px}
.content h1{font-size:14.5px;font-weight:400;line-height:19px;color:#333;text-transform:uppercase;padding-bottom:14px;border-bottom:1px solid var(--line)}
.content h1 b{color:var(--red);font-weight:700}
.content p{font-size:9.6px;line-height:14.5px;color:#666}
.content .lead{margin-top:12px}
.content .hl{color:var(--red)}
.explore{display:flex;justify-content:space-between;margin-top:42px}
.explore-list{width:290px}
.explore-list h3{font-size:13px;font-style:italic;font-weight:400;color:#333}
.explore-list h3 b{color:var(--red);font-style:normal;font-weight:700}
.explore-list ul{list-style:none;margin-top:8px}
.explore-list li{display:flex;gap:10px;font-size:9.6px;font-style:italic;line-height:13px;color:#444;padding:6px 0 7px;border-bottom:1px dashed var(--line)}
.explore-list li:last-child{border-bottom:0}
.explore-list li.hl{color:var(--red)}
.explore-list li svg{flex:0 0 12px;margin-top:1px}
.how-box{width:215px;height:140px;background:#fff;border:1px solid #e2e2e2;box-shadow:0 1px 5px rgba(0,0,0,.15);padding:8px 10px;margin-top:-30px}
.how-box h3{text-align:center;font-size:14px;font-weight:400;color:#333}
.how-box h3 b{color:var(--red);font-weight:700}
.how-video{position:relative;height:98px;margin-top:6px;background:linear-gradient(90deg,#d9c3a8,#f2ede4 50%,#c9b49a)}
.how-video svg{position:absolute;left:50%;top:50%;transform:translate(-50%,-50%)}
.body-copy{margin-top:28px}
.body-copy p{margin-bottom:14px}

.site-footer{position:absolute;left:0;top:1069px;width:1028px;height:131px;background:linear-gradient(var(--footer-top),var(--footer-bottom));color:#9a9a9a}
.footer-col{position:absolute;top:25px}
.footer-col h4{color:#fff;font-size:10px;font-weight:600;margin-bottom:6px}
.sitemap{left:126px}
.sitemap nav{font-size:9px;color:#bbb}
.sitemap nav a:first-child{color:#fff;text-decoration:underline}
.sitemap small{display:block;font-size:8.5px;margin-top:4px}
.location{left:504px;font-size:9.5px;line-height:14px}
.location::before{content:"";position:absolute;left:-24px;top:0;width:1px;height:55px;background:#555}
.social{left:793px}
.social::before{content:"";position:absolute;left:-24px;top:0;width:1px;height:55px;background:#555}
.social-row{display:flex;gap:5px;margin-top:2px}
.social-row span{width:26px;height:26px;background:#3d78b6}
.social-row span:nth-child(2){background:#39a3db}
.social-row span:nth-child(3){background:#666}
.social-row span:nth-child(4){background:#2a83b8}
</style>
</head>
<body>

<header class="site-header">
  <a class="brand" href="#"><span class="brand-dot"></span><span class="brand-name">Harbor Mortgage<br>Relief</span></a>
  <div class="hotline">Call Tall Free Now
    <strong><svg width="12" height="18" viewBox="0 0 12 18"><path d="M3 1h4l-1 5-2 1q1 4 3 5l2-1 2 4-3 2Q2 15 1 6z" fill="#e0252b"/></svg>800-555-0142</strong>
  </div>
  <nav class="main-nav">
    <a class="is-active" href="#">Home</a><a href="#">About Us</a><a href="#">Services</a><a href="#">Contact Us</a><a href="#">Financing Options</a>
  </nav>
</header>

<section class="hero" role="img" aria-label="Photo of a smiling family with a baby in front of their yellow house">
  <div class="consult">
    <h2><b>NEED</b> FREE CONSULTATION?</h2>
    <p>Simply enter your zip code below to find help in your area.</p>
    <div class="consult-form"><span>Enter Email</span><b>Send Request</b></div>
  </div>
</section>

<div class="feature-band"></div>
<div class="features">
  <div class="feature">
    <svg width="32" height="28" viewBox="0 0 32 28" fill="none" stroke="#e0252b" stroke-width="2"><rect x="11" y="2" width="10" height="7"/><path d="M16 9v5M5 14h22M5 14v4M16 14v4M27 14v4"/><rect x="1" y="18" width="8" height="7"/><rect x="12" y="18" width="8" height="7"/><rect x="23" y="18" width="8" height="7"/></svg>
    <span>Financing/Purchase<br>Options</span>
  </div>
  <div class="feature is-active">
    <svg width="32" height="28" viewBox="0 0 32 28" fill="none" stroke="#e0252b" stroke-width="2"><rect x="5" y="3" width="22" height="15"/><path d="M1 22h30"/><circle cx="16" cy="10" r="3" fill="#e0252b"/></svg>
    <span>Relocations Assistance<br>- if needed</span>
  </div>
  <div class="feature">
    <svg width="32" height="28" viewBox="0 0 32 28"><circle cx="16" cy="14" r="9" fill="none" stroke="#e0252b" stroke-width="5" stroke-dasharray="4 3"/><circle cx="16" cy="14" r="5" fill="none" stroke="#e0252b" stroke-width="2"/></svg>
    <span>Remodel your home to<br>increase it's value</span>
  </div>
  <div class="feature">
    <svg width="32" height="28" viewBox="0 0 32 28" fill="none" stroke="#e0252b" stroke-width="2"><rect x="5" y="10" width="22" height="16"/><path d="M3 10h26v-4H3zM16 6v20M16 6q-6-6-8 0M16 6q6-6 8 0"/></svg>
    <span>Many other options<br>are available</span>
  </div>
</div>

<aside class="sidebar">
  <h2 class="side-title"><span>Customer</span> Testimonials</h2>
  <p class="quote">If I had to do it all again, the only thing I would have done differently is call Harbor Relief Team first!" with the mortgage and all of the other bills too. We are so thankful that you came to our rescue. Keeping the foreclosure off of... <a href="#">more</a></p>
  <div class="author">
    <div class="author-photo" role="img" aria-label="Portrait photo of the customer"></div>
    <div><b>Maria Delgado</b><small>California</small></div>
  </div>
  <a class="btn" href="#">View all</a>
  <h2 class="side-title normal mission-title"><span>Our</span> Mission</h2>
  <div class="mission-photo" role="img" aria-label="Photo of a smiling businesswoman with colleagues in an office"></div>
  <p class="mission-text">To educate homeowners on the foreclosure process and the options available to them.</p>
  <a class="btn" href="#">Read more</a>
</aside>

<main class="content">
  <h1><b>Harbor Mortgage Relief</b> specializes in assisting homeowners who are in foreclosure</h1>
  <p class="lead">Harbor Mortgage Relief specializes in assisting homeowners who are in FORECLOSURE, by offering solid alternatives to losing your home in a Trustee Sale. Having your home foreclosed on can damage your credit for up to 7 years. Most foreclosures end with the home owner being evicted from their home, leaving them with no money, no place to live and without ample time to safely remove their possessions from their home. There is no need to have this happen to you. No matter what part of foreclosure process you are in, WE CAN HELP!<br>
  <span class="hl">If you have received a Notice of Default (NOD) or Notice of Trustee Sale (NTS), you have options. Contact us today to speak to one of our licensed specialist, and let us help you put this situation behind you.</span></p>

  <div class="explore">
    <div class="explore-list">
      <h3>Explore this site or call <b>1-888-555-0176</b> to learn:</h3>
      <ul>
        <li><svg width="12" height="12" viewBox="0 0 12 12"><circle cx="6" cy="6" r="6" fill="#5fae1e"/><path d="M5 3l3 3-3 3" stroke="#fff" stroke-width="1.6" fill="none"/></svg>what kind of mortgage help may be available for you to prevent foreclosure</li>
        <li class="hl"><svg width="12" height="12" viewBox="0 0 12 12"><circle cx="6" cy="6" r="6" fill="#5fae1e"/><path d="M5 3l3 3-3 3" stroke="#fff" stroke-width="1.6" fill="none"/></svg>if you qualify for assistance using our quick and convenient eligibility tool</li>
        <li><svg width="12" height="12" viewBox="0 0 12 12"><circle cx="6" cy="6" r="6" fill="#5fae1e"/><path d="M5 3l3 3-3 3" stroke="#fff" stroke-width="1.6" fill="none"/></svg>how to find a HUD-approved housing counseling agency in your area to help you apply and how to apply online</li>
      </ul>
    </div>
    <div class="how-box">
      <h3><b>HOW</b> IT WORKS</h3>
      <div class="how-video" role="img" aria-label="Video still of a happy family with two young children">
        <svg width="34" height="34" viewBox="0 0 34 34"><circle cx="17" cy="17" r="16" fill="rgba(0,0,0,.55)" stroke="#fff" stroke-width="2"/><path d="M13 10l11 7-11 7z" fill="#fff"/></svg>
      </div>
    </div>
  </div>

  <div class="body-copy">
    <p>We speak to hundreds of homeowners every day, we understand how frustrating this can be. Don't live in fear of what is to come. You have other options, please call or email us today and we will immediately put our specialist to work finding you a solution.</p>
    <p>Don't try to handle this frustrating situation by yourself. <span class="hl">Harbor Mortgage Relief is a team of knowledgeable real estate professionals, we can offer you a better solution during this tough time.</span></p>
    <p>Harbor Mortgage Relief has been assisting families in foreclosure for years. Our skill and integrity has earned us a reputation for fast, professional, courteous and thorough solutions. With over 50 years of real estate knowledge and experience HARBOR MORTGAGE RELIEF is ready to assist you.</p>
  </div>
</main>

<footer class="site-footer">
  <div class="footer-col sitemap">
    <h4>Site map</h4>
    <nav><a href="#">HOME</a> / ABOUT US / SERVICES / CONTACT US / FINANCING OPTIONS</nav>
    <small>Content copyright 2012. harbormortgagerelief.com. All rights reserved.</small>
  </div>
  <div class="footer-col location">
    <h4>Our location</h4>
    Harbor Mortgage Relief<br>215 Harbor View Drive Suite 300 San Diego, CA 92101
  </div>
  <div class="footer-col social">
    <h4>Find us on</h4>
    <div class="social-row"><span></span><span></span><span></span><span></span></div>
  </div>
</footer>

</body>
</html>
```